Math Help Website Needs New Design

Looking to refresh the design of my existing site (quillnumberdesk.com) to be easier on the eyes. I am fully capable of doing the HTML coding and have for years, but I don't have the eye for good design, colors, layout, and fonts. This is where I need help!

I need both a new design scheme and a new logo that matches. The overall functionality will be the same as the existing site, and should not be unrecognizable.

Target Market(s)

It should appeal to students (age 13-22) and their parents, so it should NOT be childish in appearance, nor should it be corporate.

Requirements
Must have
• Should be simple, easy-to-navigate, and neither childish nor corporate. I am looking for a design for both the homepage and a similar "content" page. Simple, bold colors are preferred. A logo should be prominent at the top, with a search bar nearby. Below that I need a similar navigational area like I already have. Then, I need about 200px wide ad space on the left of the main body area.

```html
<!DOCTYPE html>
<html lang="en">
<head>
<meta charset="utf-8">
<title>Quill Number Desk — Message Board</title>
<link href="https://fonts.googleapis.com/css2?family=Mulish:wght@300;400;600;800&family=Arimo:wght@400;700&display=swap" rel="stylesheet">
<style>
:root{
  --bg:#13252f;
  --bg-footer:#162b36;
  --green:#4fdc8e;
  --link:#7cf0ae;
  --white:#ffffff;
  --text:#e6eef0;
  --muted:#5f7c84;
  --rule:#3e5861;
  --hero-a:#1d3a46;
  --hero-b:#2b5a52;
}
*{margin:0;padding:0;box-sizing:border-box}
html,body{width:823px;height:1200px;overflow:hidden;background:var(--bg)}
body{position:relative;font-family:"Mulish",sans-serif;color:var(--text)}
a{text-decoration:none;color:inherit}
.abs{position:absolute}

.brand{left:84px;top:92px;font-weight:800;font-size:34px;color:var(--white);letter-spacing:-.5px;display:flex;align-items:center;gap:10px}
.brand-dot{width:22px;height:22px;border-radius:50%;background:var(--green)}

.search{left:512px;top:111px;width:245px;height:31px;border-radius:16px;background:var(--white);display:flex;align-items:center;padding-left:12px;gap:8px;font-size:17px;color:#8a8f92}

.nav{top:180px;left:66px;right:66px;display:flex;font-size:19px;font-family:"Arimo",sans-serif}
.nav a{color:var(--green);margin-right:12px}
.nav a.current{color:var(--white)}
.nav a.board{margin-left:auto;margin-right:0}

.hero{left:0;top:221px;width:823px;height:191px;background:linear-gradient(90deg,var(--hero-a) 0%,var(--hero-b) 35%,var(--bg) 75%)}
.hero-art{left:0;top:221px;width:380px;height:191px;background:radial-gradient(ellipse at 45% 50%,#3c4a50 0%,#25353c 55%,rgba(29,58,70,0) 100%)}
.hero-copy{right:66px;top:232px;text-align:right;width:520px}
.hero-copy h1{font-weight:300;font-size:31px;color:var(--white);line-height:48px;white-space:nowrap}
.hero-copy p{font-size:15.5px;line-height:19px;color:var(--text);margin-top:4px;margin-left:auto;width:372px}
.hero-copy p.lead{color:var(--green);font-size:16.5px;font-weight:600;margin-top:6px;line-height:19.5px;width:360px}

.board-title{left:304px;top:415px;font-size:32px;font-weight:300;color:var(--white)}
.ico{position:absolute}
.ask-title{left:299px;top:475px;font-size:21px;font-weight:300;color:var(--white)}
.ask-text{left:297px;top:510px;width:282px;font-size:12.5px;line-height:16px;color:var(--white)}
.disc-title{left:299px;top:596px;font-size:18.5px;font-weight:400;color:var(--white);font-family:"Arimo",sans-serif}

.threads{left:297px;top:633px;width:276px;list-style:none;font-family:"Arimo",sans-serif}
.threads li{height:29px;border-top:1px solid var(--rule);padding-top:3px}
.threads li:last-child{border-bottom:1px solid var(--rule)}
.threads .t{display:block;font-weight:700;font-size:12px;color:var(--link);line-height:13px;white-space:nowrap}
.threads .by{display:block;font-size:8.5px;font-weight:700;color:var(--muted);line-height:9px}
.threads .by.fresh{color:var(--white)}

.side{left:599px;width:158px}
.dash{height:0;border-top:1px dashed #8fa3a8}
.side h3{font-size:16px;font-weight:600;color:var(--white);font-family:"Arimo",sans-serif}
.news{list-style:none;font-family:"Arimo",sans-serif}
.news li{display:flex;gap:5px;font-size:10.5px;font-weight:700;color:var(--white);line-height:11px;margin-bottom:9px}
.news .plus{flex:none;width:12px;height:12px;border-radius:50%;background:var(--green);color:var(--bg);font-size:11px;line-height:12px;text-align:center}
.lessons{list-style:none;font-family:"Arimo",sans-serif}
.lessons li{font-size:13px;line-height:21px;color:var(--green)}

.footer{left:0;top:1083px;width:823px;height:117px;background:var(--bg-footer)}
.footer-brand{right:80px;top:1124px;font-weight:800;font-size:16px;color:var(--white)}
</style>
</head>
<body>

<div class="abs brand"><span class="brand-dot"></span>Quill Number Desk</div>

<div class="abs search">
  <svg width="16" height="18" viewBox="0 0 16 18"><circle cx="7" cy="7" r="5.5" fill="none" stroke="#9aa0a3" stroke-width="2"/><line x1="7" y1="12.5" x2="7" y2="17" stroke="#9aa0a3" stroke-width="2.5"/></svg>
  Search
</div>

<nav class="abs nav">
  <a class="current" href="#">Home</a>
  <a href="#">Algebra</a>
  <a href="#">Geometry</a>
  <a href="#">Trig</a>
  <a href="#">Calculus</a>
  <a href="#">Statistics</a>
  <a href="#">More</a>
  <a class="board" href="#">Message Board</a>
</nav>

<div class="abs hero"></div>
<div class="abs hero-art" role="img" aria-label="Banner illustration area"></div>
<div class="abs hero-copy">
  <h1>Welcome to Quill Number Desk.</h1>
  <p>Math Lessons - Looking to understand a subject better, or maybe you don't understand what your textbook is trying to tell you?</p>
  <p class="lead">We have a collection of algebra and geometry lessons that you can view online right now.</p>
</div>

<svg class="ico" style="left:252px;top:396px" width="46" height="46" viewBox="0 0 46 46">
  <path d="M4 12 h34 v22 h-18 l-8 8 v-8 h-8z" fill="#fff"/>
  <path d="M22 26 l14-18 4 3-14 18-5 1z" fill="#fff" stroke="#13252f" stroke-width="1.5"/>
</svg>
<h2 class="abs board-title">Message Board</h2>

<svg class="ico" style="left:270px;top:470px" width="20" height="30" viewBox="0 0 20 30"><path d="M14 2 l4 3 -12 20 -4 2 0-5z" fill="#fff"/></svg>
<h3 class="abs ask-title">Ask your question</h3>
<p class="abs ask-text">Ask your question on our math help message board. Just be sure to explain what you've tried to do and where you're stuck, and a friendly volunteer may try to assist you!</p>

<svg class="ico" style="left:257px;top:585px" width="36" height="32" viewBox="0 0 36 32"><path d="M2 3 h32 v20 h-16 l-6 7 v-7 h-10z" fill="#fff"/></svg>
<h3 class="abs disc-title">Current Discussions</h3>

<ul class="abs threads">
  <li><a class="t" href="#">New 1000 challenge!</a><span class="by fresh">Posted by: tallyfox</span></li>
  <li><a class="t" href="#">Moved - word problem - Mixture/Solution</a><span class="by fresh">Posted by: Brookmere</span></li>
  <li><a class="t" href="#">graphing exponential functions where ...</a><span class="by">Posted by: Brookmere</span></li>
  <li><a class="t" href="#">Simplifying Question -- Please Help?</a><span class="by">Posted by: Orrin Vale</span></li>
  <li><a class="t" href="#">Real world Radical Formula???</a><span class="by">Posted by:qvmark</span></li>
  <li><a class="t" href="#">Maths for biz</a><span class="by">Posted by: ferngrid</span></li>
  <li><a class="t" href="#">Island Math tutorials</a><span class="by">Posted by: Tobin</span></li>
  <li><a class="t" href="#">simple probability (two questions)</a><span class="by">Posted by: PaulR</span></li>
  <li><a class="t" href="#">Rotation Around Y=2</a><span class="by">Posted by: LenaQ</span></li>
  <li><a class="t" href="#">Calculus - box problem</a><span class="by">Posted by: Pinecob2</span></li>
  <li><a class="t" href="#">finding an oblique asymptote</a><span class="by">Posted by: PaulR</span></li>
  <li><a class="t" href="#">Volume - Washer Method</a><span class="by">Posted by: LenaQ</span></li>
  <li><a class="t" href="#">How to solve this</a><span class="by">Posted by: Huxley31</span></li>
  <li><a class="t" href="#">Volume -Revolved Around y=2</a><span class="by">Posted by: morwent</span></li>
  <li><a class="t" href="#">Volume of solid bound by Trig function</a><span class="by">Posted by: LenaQ</span></li>
</ul>

<div class="abs side dash" style="top:431px"></div>
<h3 class="abs side" style="top:448px">Whats new?</h3>
<ul class="abs side news" style="top:482px">
  <li><span class="plus">+</span>Multiplying Polynomials</li>
  <li><span class="plus">+</span>Derivative of an Inverse Function</li>
  <li><span class="plus">+</span>Derivatives of Logs and Exps</li>
  <li><span class="plus">+</span>Differentiating Trig Functions</li>
</ul>

<div class="abs side dash" style="top:616px"></div>
<h3 class="abs side" style="top:634px;left:602px">Math Lessons</h3>
<ul class="abs side lessons" style="top:666px;left:601px">
  <li><a href="#">Algebra</a></li>
  <li><a href="#">Geometry</a></li>
  <li><a href="#">Trigonometry</a></li>
  <li><a href="#">Calculus</a></li>
  <li><a href="#">Statistics</a></li>
  <li><a href="#">Sports Math</a></li>
  <li><a href="#">Math Games</a></li>
  <li><a href="#">Calculators</a></li>
</ul>

<footer class="abs footer"></footer>
<div class="abs footer-brand">Quill Number Desk</div>

</body>
</html>
```